Need a business cards for a hair dressing salon.

Target Market(s)

Target woman for Hair cuts, bridal makeup, occasion, fashion makeup and etc.

Industry/Entity Type

Hair

Font styles to use
Serif
Script

Requirements
Must have
• - Business card to be memorable and recognizable

- Please include the following on the business card:
- Business name: Salon Marolin
- Name: Nilumi Jayasekara (Name Must be changeable)
- Occupation: Hair Dresser & Beautician
- Contact number: 04 731 6 CURL
- Email: mail@marolin.com.au
- Facebook (please use image): www.circlepage.com/marolin.com.au
Nice to have
• Font Styles:
Business Name - Script
Other Text - Serif

```html
<!DOCTYPE html>
<html lang="en">
<head>
<meta charset="utf-8">
<title>Salon Marolin – Business Card</title>
<link href="https://fonts.googleapis.com/css2?family=Pinyon+Script&family=Tinos&display=swap" rel="stylesheet">
<style>
  :root {
    --backdrop: #808080;
    --band-black: #000000;
    --band-sheen: #262626;
    --rule: #bdbdbd;
    --glow: #a8673f;
    --brown-mid: #4a2d26;
    --brown-deep: #1a0e0c;
    --red-deep: #3a1614;
    --text-light: #e9e6e3;
    --icon-blue: #2c5aa0;
    --icon-white: #f4f4f4;
  }
  * { margin: 0; padding: 0; box-sizing: border-box; }
  html, body {
    width: 1200px; height: 1000px; overflow: hidden;
    background: var(--backdrop);
  }
  .business-card {
    position: absolute; left: 218px; top: 283px;
    width: 761px; height: 435px;
    overflow: hidden;
    box-shadow: 0 0 2px rgba(0,0,0,.4);
  }
  .card-header {
    position: absolute; left: 0; top: 0; width: 100%; height: 120px;
    background: radial-gradient(ellipse 320px 90px at 300px 0, var(--band-sheen), var(--band-black));
    border-bottom: 1px solid var(--rule);
  }
  .salon-name {
    position: absolute; left: 24px; top: 14px;
    font-family: "Pinyon Script", cursive;
    font-size: 40px; line-height: 1;
    text-transform: uppercase;
    color: var(--text-light);
    white-space: nowrap;
    transform: scaleX(0.78);
    transform-origin: left top;
  }
  .stylist-name {
    position: absolute; left: 25px; top: 75px;
    font-family: "Tinos", serif;
    font-size: 24px; letter-spacing: 3.6px;
    text-transform: uppercase;
    color: var(--text-light);
    white-space: nowrap;
  }
  .card-body {
    position: absolute; left: 0; top: 121px; width: 100%; height: 314px;
    background:
      radial-gradient(ellipse 260px 170px at 365px 10px, var(--glow), rgba(168,103,63,0) 100%),
      radial-gradient(ellipse 420px 260px at 380px 320px, var(--red-deep), rgba(58,22,20,0) 100%),
      radial-gradient(ellipse 480px 300px at 370px 80px, var(--brown-mid), var(--brown-deep));
  }
  .occupation {
    position: absolute; left: 0; top: 54px; width: 100%;
    text-align: center;
    font-family: "Tinos", serif;
    font-size: 25px; letter-spacing: 5px;
    text-transform: uppercase;
    color: var(--text-light);
    white-space: nowrap;
  }
  .contact-list {
    position: absolute; left: 229px; top: 197px;
    list-style: none;
  }
  .contact-item {
    display: flex; align-items: center;
    height: 20px; margin-bottom: 14px;
    font-family: "Tinos", serif;
    font-size: 19px; letter-spacing: 2.5px;
    text-transform: uppercase;
    color: var(--text-light);
    white-space: nowrap;
  }
  .contact-item:last-child { margin-top: 3px; }
  .contact-icon { width: 22px; height: 22px; margin-right: 14px; flex: none; }
</style>
</head>
<body>
  <div class="business-card">
    <header class="card-header">
      <div class="salon-name">Salon Marolin</div>
      <div class="stylist-name">Nilumi Jayasekara</div>
    </header>
    <section class="card-body">
      <div class="occupation">Hair Dresser &amp; Beautician</div>
      <ul class="contact-list">
        <li class="contact-item">
          <svg class="contact-icon" viewBox="0 0 22 22" aria-hidden="true">
            <rect width="22" height="22" rx="4" fill="var(--icon-blue)"/>
            <path d="M7 5c1 0 1.8 2 2 3s-1 1.3-.8 2c.5 1.3 1.5 2.4 2.8 3 .7.2 1-1 2-.8s3 1 3 2-1.5 2.4-3 2.2C9 15.8 6.2 13 5.4 9 5 7 6 5 7 5z" fill="var(--icon-white)"/>
          </svg>
          04 731 6 CURL
        </li>
        <li class="contact-item">
          <svg class="contact-icon" viewBox="0 0 22 22" aria-hidden="true">
            <rect x="1" y="4" width="20" height="15" rx="2" fill="var(--icon-white)"/>
            <path d="M1 7l10 7 10-7" fill="none" stroke="#c9c9c9" stroke-width="1"/>
            <circle cx="11" cy="9" r="3" fill="none" stroke="var(--icon-blue)" stroke-width="1.4"/>
          </svg>
          mail@marolin.com.au
        </li>
        <li class="contact-item">
          <svg class="contact-icon" viewBox="0 0 22 22" aria-hidden="true">
            <rect width="20" height="20" x="1" y="1" fill="var(--icon-blue)"/>
          </svg>
          www.circlepage.com/marolin.com.au
        </li>
      </ul>
    </section>
  </div>
</body>
</html>
```